TEK Logistics - Banner 2.5' x 8' for 20+ locations

Need a banner designed that will pop. This banner will be displayed at over 20 of our transportation facilities. Goal is for the banner to grab the attention of employees, contractors and clients and help reinforce our mission and core values. Designed needs to include TEK Logo, our core values and mission statement. Red and Black are the main company colors and we need to stay within that theme and color pallet. Attached is a previous version that was too basic and boring. Willing to consider a design that excludes the mission statement.

Gathering more feedback

```html
<!DOCTYPE html>
<html lang="en">
<head>
<meta charset="utf-8">
<title>TEK Logistics – Core Values Banner</title>
<link href="https://fonts.googleapis.com/css2?family=Bebas+Neue&display=swap" rel="stylesheet">
<style>
  :root {
    --page-bg: #f3f3f3;
    --banner-white: #ffffff;
    --brand-red: #d42a2a;
    --brand-red-deep: #8c0a0c;
    --brand-black: #111111;
    --value-yellow: #f6ea15;
    --value-white: #ffffff;
  }
  * { margin: 0; padding: 0; box-sizing: border-box; }
  html, body {
    width: 1121px;
    height: 1200px;
    overflow: hidden;
    background: var(--page-bg);
    font-family: "Bebas Neue", "Arial Narrow", sans-serif;
  }
  .banner {
    position: absolute;
    left: 30px;
    top: 434px;
    width: 1061px;
    height: 332px;
    overflow: hidden;
    background: var(--banner-white);
    box-shadow: 0 28px 40px -12px rgba(0, 0, 0, 0.35);
  }
  .banner-art {
    position: absolute;
    inset: 0;
    width: 100%;
    height: 100%;
  }
  .brand-name {
    position: absolute;
    left: 40px;
    top: 110px;
    width: 190px;
    text-align: center;
    color: var(--brand-red);
    line-height: 0.9;
  }
  .brand-name .brand-main {
    display: block;
    font-size: 78px;
    letter-spacing: 2px;
  }
  .brand-name .brand-sub {
    display: block;
    font-size: 30px;
    letter-spacing: 5px;
  }
  .value {
    position: absolute;
    padding-left: 22px;
    font-size: 37px;
    line-height: 36px;
    white-space: nowrap;
  }
  .value::before {
    content: "";
    position: absolute;
    left: 0;
    top: 2px;
    width: 6px;
    height: 64px;
    background: var(--value-white);
  }
  .value .accent { color: var(--value-yellow); display: block; }
  .value .plain { color: var(--value-white); display: block; }
  .col-left { left: 436px; }
  .col-right { left: 781px; }
  .row-1 { top: 28px; }
  .row-2 { top: 130px; }
  .row-3 { top: 231px; }
</style>
</head>
<body>
  <section class="banner" aria-label="TEK Logistics core values banner">
    <svg class="banner-art" viewBox="0 0 1061 332" preserveAspectRatio="none" aria-hidden="true">
      <defs>
        <linearGradient id="redFade" x1="0" y1="0" x2="0" y2="1">
          <stop offset="0" stop-color="#d42a2a"/>
          <stop offset="1" stop-color="#8c0a0c"/>
        </linearGradient>
      </defs>
      <polygon class="divider-band" points="372,0 388,0 268,332 252,332" fill="var(--brand-black)"/>
      <polygon class="value-field" points="400,0 1061,0 1061,332 280,332" fill="url(#redFade)"/>
    </svg>

    <div class="brand-name">
      <span class="brand-main">TEK</span>
      <span class="brand-sub">LOGISTICS</span>
    </div>

    <div class="value col-left row-1"><span class="accent">DO THE RIGHT THINGS</span><span class="plain">FOR THE RIGHT REASONS</span></div>
    <div class="value col-left row-2"><span class="accent">PURSUE GROWTH</span><span class="plain">AND DEVELOPMENT</span></div>
    <div class="value col-left row-3"><span class="accent">BUILD A POSITIVE</span><span class="plain">TEAM ATMOSPHERE</span></div>

    <div class="value col-right row-1"><span class="accent">DELIVER WOW</span><span class="plain">THROUGH SERVICE</span></div>
    <div class="value col-right row-2"><span class="plain">DO EVERYTHING</span><span class="accent">SAFELY</span></div>
    <div class="value col-right row-3"><span class="plain">HAVE</span><span class="accent">FUN</span></div>
  </section>
</body>
</html>
```